Broschüre
Zielgruppe
Wir sind eine ambulanter Pflegedienst in Rostock. Ab dem Herbst 25 bieten wir für Interessenten mit einem Pflegegrad begleitete reisen an. Eine Fachkraft wird Patienten mit Pflegegrad in kleinen Gruppen begleiten. Den Text für den Flyer haben wir eingefügt. Bitte die Bider aus dem Stock Portal wählen. Über den Flyer sollen Patienten gefunden werden.
Der Flyer
sollte Serios wirken und Reiselust der Senioren wecken.
Aufgabenstellung
Hier der Text für den Flyer:
Was wir bieten:
✔️ Begleitung durch erfahrene Pflegefachkräfte ✔️ Körperpflege, Medikamentengabe & Betreuung wie zuhause ✔️ 24-Stunden-Erreichbarkeit unserer Pflegekräfte vor Ort im gebuchten Hotel ✔️ Zusammenarbeit mit ausgewählten Hotels – barrierefrei & seniorengerecht ✔️ Kleine Gruppen & individuelle Betreuung vor Ort
Gut zu wissen:
Für unsere pflegerische Begleitung entstehen Ihnen keine zusätzlichen Kosten, wenn Sie einen Pflegegrad haben und das Verhinderungspflege-Budget noch nicht aufgebraucht ist.
Lediglich die Hotelkosten sind von Ihnen selbst zu tragen.
Wer hat Anspruch auf Verhinderungspflege?
Alle Pflegebedürftigen mit einem anerkannten Pflegegrad ab Stufe 2 können jährlich Verhinderungspflege über die Pflegekasse abrufen – ideal, um sich im Urlaub sicher begleiten zu lassen!
Unser Service – Ihr Mehrwert:
Wir organisieren Ihre Reise von A bis Z und begleiten Sie oder Ihre Angehörigen auf dem Weg zu Erholung und neuen Eindrücken – mit Herz, Kompetenz und Erfahrung. Vor Ort sind müssen Sie auf nichts verzichten und werden versorgt wie zu Hause. Gerne organisieren wir auch die Abholung aus ihrer Hässlichkeit.
???? Seniorenhafen Touren – Ihr verlässlicher Partner für Pflege und Lebensfreude
???? Jetzt informieren & Platz sichern: 0381 - 52794163
???? Mail@seniorenhafen-touren .de
???? www.seniorenhafen-touren.de

```html
<!DOCTYPE html>
<html lang="de">
<head>
<meta charset="utf-8">
<title>Begleitete Reisen – Seniorenhafen Touren</title>
<link rel="stylesheet" href="https://fonts.googleapis.com/css2?family=Libre+Caslon+Text:wght@400&family=Inter:wght@400;600&display=swap">
<style>
  :root{
    --teal:#5e8e86;
    --teal-dark:#4a7a72;
    --teal-soft:#dfe9e6;
    --gold:#c9a96e;
    --gold-light:#e3cf9f;
    --mist:#eef2f1;
    --paper:#ffffff;
    --ink:#3b3f40;
    --serif:"Libre Caslon Text", Georgia, serif;
    --sans:"Inter", Arial, sans-serif;
  }
  *{box-sizing:border-box;margin:0;padding:0}
  html,body{width:1200px;height:900px;overflow:hidden;background:var(--paper)}
  .flyer{position:relative;width:1200px;height:900px;overflow:hidden;font-family:var(--sans);color:var(--ink)}
  .backdrop{position:absolute;inset:0}
  .brand{position:absolute;left:34px;top:34px;font-family:var(--serif);font-size:30px;color:var(--teal-dark);z-index:2}
  .cover-title{position:absolute;left:0;width:600px;top:540px;text-align:center;font-family:var(--serif);font-size:66px;line-height:1.08;color:#fff;font-weight:400}
  .cover-sub{position:absolute;left:0;width:600px;top:782px;text-align:center;font-size:20px;line-height:1.45;color:#fff}
  .tile{position:absolute;border-radius:8px}
  .tile--teal{background:var(--teal)}
  .tile--gold{background:var(--gold)}
  .tile--mist{background:var(--teal-soft)}
  .tile-label{position:absolute;left:0;right:0;bottom:24px;text-align:center;color:#fff;font-weight:600;font-size:12px;letter-spacing:.5px}
  .tile svg{position:absolute;inset:0;width:100%;height:100%}
  .photo{position:absolute;border-radius:6px}
  .photo--beach{left:650px;top:375px;width:148px;height:92px;background:linear-gradient(180deg,#4b7fb8 0%,#9bb8d2 45%,#c77b45 70%,#b6895e 100%)}
  .photo--tower{left:748px;top:493px;width:85px;height:88px;background:linear-gradient(160deg,#c6d3de,#8d9a6a 55%,#6b6b45)}
  .photo--tubes{left:770px;top:298px;width:63px;height:170px;background:linear-gradient(90deg,#f2f2f2,#ffffff 50%,#e6e6e6);border-radius:10px}
  .note{position:absolute;left:650px;top:702px;width:183px;height:98px;background:var(--mist);border-radius:8px;padding:16px 14px;font-size:14px;line-height:1.5;color:var(--teal-dark)}
  .intro-title{position:absolute;left:875px;top:52px;width:300px;font-family:var(--serif);font-size:22px;line-height:1.3;color:var(--ink);font-weight:400}
  .intro-text{position:absolute;left:875px;top:140px;width:300px;font-size:14px;line-height:23px;color:var(--ink)}
  .aside-text{position:absolute;left:905px;top:520px;width:230px;font-size:14.5px;line-height:1.55;color:var(--teal-dark)}
  .launch{position:absolute;left:922px;top:752px;width:260px;font-size:13px;line-height:1.5;color:#fff}
  .cta{position:absolute;left:920px;top:810px;width:175px;height:46px;background:#fff;border-radius:6px;display:flex;align-items:center;justify-content:center;gap:8px;font-size:14px;color:var(--teal-dark);font-weight:600}
</style>
</head>
<body>
<main class="flyer">
  <svg class="backdrop" width="1200" height="900" viewBox="0 0 1200 900" aria-hidden="true">
    <defs>
      <linearGradient id="heroTone" x1="0" y1="0" x2="1" y2="1">
        <stop offset="0" stop-color="#cfe0ee"/>
        <stop offset=".45" stop-color="#e6d8c2"/>
        <stop offset="1" stop-color="#8aa07a"/>
      </linearGradient>
    </defs>
    <rect x="0" y="0" width="600" height="900" fill="var(--teal)"/>
    <rect x="600" y="600" width="600" height="300" fill="var(--teal)"/>
    <path d="M600 0 H1200 V640 C1080 690 960 700 850 760 C760 810 700 860 600 900 Z" fill="var(--paper)"/>
    <path d="M880 470 C1000 445 1120 450 1200 470 V640 C1100 665 990 700 900 650 Z" fill="var(--mist)"/>
    <path d="M600 880 C700 850 760 800 850 760 C960 700 1080 670 1200 640" fill="none" stroke="var(--gold-light)" stroke-width="6"/>
  </svg>

  <svg style="position:absolute;left:0;top:0" width="600" height="520" viewBox="0 0 600 520" role="img" aria-label="Foto: lächelndes Seniorenpaar mit einer Pflegekraft auf einer sonnigen Terrasse am See">
    <path d="M0 0 H600 V330 C500 380 400 480 250 480 C150 480 60 450 0 440 Z" fill="url(#heroTone)"/>
    <path d="M0 440 C60 450 150 480 250 480 C400 480 500 380 600 330" fill="none" stroke="var(--gold)" stroke-width="6"/>
  </svg>

  <div class="brand">Seniorenhafen Touren</div>

  <h1 class="cover-title">Begleitete<br>Reisen mit<br>Pflegegrad</h1>
  <p class="cover-sub">Ab Herbst 2025<br>aus Rostock</p>

  <div class="tile tile--teal" style="left:650px;top:55px;width:85px;height:180px">
    <svg viewBox="0 0 85 180" aria-hidden="true">
      <circle cx="42.5" cy="135" r="20" fill="none" stroke="#fff" stroke-width="1.5"/>
      <circle cx="42.5" cy="60" r="14" fill="none" stroke="#fff" stroke-width="1.5"/>
    </svg>
  </div>
  <div class="tile tile--teal" role="img" aria-label="Dekorative Form" style="left:752px;top:45px;width:82px;height:75px;border-radius:40px 12px 40px 12px"></div>
  <div class="tile tile--gold" style="left:748px;top:147px;width:85px;height:90px">
    <svg viewBox="0 0 85 90" aria-hidden="true">
      <path d="M42.5 25 V45 M30 32 L42.5 45 L55 32" fill="none" stroke="#fff" stroke-width="1.5"/>
    </svg>
    <span class="tile-label">PFLEGE</span>
  </div>
  <div class="tile tile--mist" style="left:650px;top:262px;width:85px;height:88px">
    <svg viewBox="0 0 85 88" aria-hidden="true">
      <path d="M22 60 V34 M30 60 V44 M38 60 V38 M48 60 V34 M56 60 V46 M64 60 V36 M20 60 H66" fill="none" stroke="var(--teal-dark)" stroke-width="2.5"/>
    </svg>
  </div>
  <div class="photo photo--tubes" role="img" aria-label="Produktfoto: weiße Pflegetuben"></div>
  <div class="photo photo--beach" role="img" aria-label="Foto: Senioren beim Strandspaziergang im Abendlicht"></div>
  <div class="tile tile--mist" style="left:650px;top:493px;width:85px;height:88px">
    <svg viewBox="0 0 85 88" aria-hidden="true">
      <circle cx="42.5" cy="44" r="6" fill="var(--gold)"/>
      <circle cx="42.5" cy="44" r="20" fill="none" stroke="var(--teal)" stroke-width="6" stroke-dasharray="8 7"/>
    </svg>
  </div>
  <div class="photo photo--tower" role="img" aria-label="Foto: historischer Turm zwischen Herbstbäumen"></div>
  <div class="tile tile--gold" style="left:650px;top:606px;width:85px;height:88px">
    <svg viewBox="0 0 85 88" aria-hidden="true">
      <circle cx="36" cy="38" r="7" fill="#fff"/><circle cx="50" cy="38" r="7" fill="#fff"/>
      <circle cx="43" cy="56" r="9" fill="#fff"/>
    </svg>
  </div>
  <div class="tile tile--mist" style="left:748px;top:606px;width:85px;height:110px">
    <svg viewBox="0 0 85 110" aria-hidden="true">
      <circle cx="42.5" cy="50" r="18" fill="none" stroke="var(--teal)" stroke-width="7"/>
    </svg>
  </div>
  <div class="note">Gut zu wissen: keine Zusatzkosten für die Pflege.</div>

  <h2 class="intro-title">Begleitete Reisen für<br>Einzelne &amp; Gruppen.</h2>
  <p class="intro-text">Begleitung durch erfahrene Pflegefachkräfte, Körperpflege, Medikamentengabe und Betreuung wie zuhause. Unsere Pflegekräfte sind im gebuchten Hotel rund um die Uhr erreichbar. Wir arbeiten mit ausgewählten Hotels, barrierefrei und seniorengerecht, reisen in kleinen Gruppen und organisieren Ihre Reise von A bis Z – auf Wunsch mit Abholung von zu Hause.</p>

  <svg style="position:absolute;left:1106px;top:463px" width="50" height="50" viewBox="0 0 50 50" aria-hidden="true">
    <circle cx="25" cy="25" r="25" fill="var(--gold)"/>
    <path d="M25 15 V35 M15 25 H35" stroke="#fff" stroke-width="3"/>
  </svg>
  <p class="aside-text">Verhinderungspflege ab Pflegegrad 2 – jährlich über die Pflegekasse abrufbar.</p>

  <p class="launch">Jetzt informieren &amp; Platz sichern:<br>0381 - 52794163</p>
  <div class="cta">
    <svg width="12" height="14" viewBox="0 0 12 14" aria-hidden="true"><path d="M6 0 V10 M1 6 L6 12 L11 6" fill="none" stroke="var(--teal-dark)" stroke-width="2"/></svg>
    Platz sichern
  </div>
</main>
</body>
</html>
```